PWR Business Card

Looking for a business card for my restaurant group I own. Four different concepts:

Copperleaf Alehouse
Bramble Alehouse
Hollister's Wood Fired Grill
Fenwick Patty Company

Card doesn't need to include all the logos.

```html
<!DOCTYPE html>
<html lang="en">
<head>
<meta charset="utf-8">
<title>PWR Business Card</title>
<link rel="stylesheet" href="https://fonts.googleapis.com/css2?family=Open+Sans:wght@400;700&display=swap">
<style>
  :root {
    --backdrop: #3a3b3d;
    --card-black: #161616;
    --slate: #77787b;
    --gold: #d4b36a;
    --white: #ffffff;
  }
  html, body {
    margin: 0;
    padding: 0;
    width: 1200px;
    height: 900px;
    overflow: hidden;
    background: var(--backdrop);
    font-family: "Open Sans", sans-serif;
  }
  .stage {
    position: relative;
    width: 1200px;
    height: 900px;
  }
  .card {
    position: absolute;
    left: 300px;
    width: 600px;
    height: 343px;
    border-radius: 26px;
    overflow: hidden;
    background: var(--card-black);
    box-shadow: 0 14px 30px rgba(0,0,0,0.45);
  }
  .card-front { top: 68px; }
  .card-back { top: 489px; }

  .front-edge {
    position: absolute;
    left: 0; right: 0; bottom: 0;
    height: 14px;
    background: var(--gold);
  }
  .brand-mark {
    position: absolute;
    display: flex;
    flex-direction: column;
    align-items: center;
    color: var(--gold);
    font-weight: 700;
    text-align: center;
  }
  .card-front .brand-mark {
    left: 0; right: 0; top: 96px;
  }
  .brand-initials {
    display: flex;
    align-items: center;
    gap: 10px;
    font-size: 58px;
    letter-spacing: 4px;
    line-height: 1;
  }
  .brand-square {
    width: 14px;
    height: 14px;
    background: var(--gold);
  }
  .brand-name {
    margin-top: 12px;
    font-size: 20px;
    letter-spacing: 3px;
    text-transform: uppercase;
    line-height: 1.2;
  }

  .back-art {
    position: absolute;
    inset: 0;
  }
  .holder-name {
    position: absolute;
    right: 124px;
    top: 30px;
    color: var(--gold);
    font-weight: 700;
    font-size: 28px;
    line-height: 1.2;
    white-space: nowrap;
  }
  .card-back .brand-mark {
    left: 46px;
    top: 186px;
    align-items: flex-start;
    text-align: left;
  }
  .card-back .brand-initials { font-size: 34px; gap: 8px; letter-spacing: 3px; }
  .card-back .brand-square { width: 9px; height: 9px; }
  .card-back .brand-name { font-size: 11px; letter-spacing: 2px; margin-top: 6px; }

  .contact-list {
    position: absolute;
    left: 46px;
    bottom: 26px;
    margin: 0;
    padding: 0;
    list-style: none;
    color: var(--white);
    font-size: 14px;
    line-height: 22px;
  }
  .contact-list li {
    display: flex;
    align-items: center;
    gap: 10px;
  }
  .contact-list svg { width: 13px; height: 13px; flex: none; }
  .company-line {
    position: absolute;
    right: 40px;
    bottom: 74px;
    color: var(--white);
    font-size: 14px;
  }
</style>
</head>
<body>
<main class="stage">
  <section class="card card-front">
    <div class="brand-mark">
      <div class="brand-initials"><span class="brand-square"></span>PWR</div>
      <div class="brand-name">Pinewater Hospitality Group</div>
    </div>
    <div class="front-edge"></div>
  </section>

  <section class="card card-back">
    <svg class="back-art" viewBox="0 0 600 343" preserveAspectRatio="none" aria-hidden="true">
      <rect width="600" height="343" fill="var(--slate)"/>
      <path d="M0,215 C60,130 180,112 300,110 C430,108 560,95 600,25 L600,343 L0,343 Z" fill="var(--card-black)"/>
      <path d="M0,200 C60,118 180,100 300,98 C430,96 560,84 600,14" fill="none" stroke="var(--gold)" stroke-width="11"/>
      <path d="M0,214 C60,133 180,114 300,112 C430,110 560,97 600,28" fill="none" stroke="var(--gold)" stroke-width="3"/>
    </svg>
    <div class="holder-name">Evan Marsh</div>
    <div class="brand-mark">
      <div class="brand-initials"><span class="brand-square"></span>PWR</div>
      <div class="brand-name">Pinewater Hospitality Group</div>
    </div>
    <ul class="contact-list">
      <li>
        <svg viewBox="0 0 24 24"><path fill="var(--gold)" d="M6.6 10.8a15 15 0 0 0 6.6 6.6l2.2-2.2a1 1 0 0 1 1-.25 11.4 11.4 0 0 0 3.6.57 1 1 0 0 1 1 1V20a1 1 0 0 1-1 1A17 17 0 0 1 3 4a1 1 0 0 1 1-1h3.5a1 1 0 0 1 1 1c0 1.25.2 2.45.57 3.570a1 1 0 0 1-.25 1z"/></svg>
        555-210-4417
      </li>
      <li>
        <svg viewBox="0 0 24 24"><rect x="2" y="5" width="20" height="14" rx="1.5" fill="var(--gold)"/><path d="M3 6l9 7 9-7" fill="none" stroke="var(--card-black)" stroke-width="2"/></svg>
        evan@pwrkitchens.com
      </li>
      <li>
        <svg viewBox="0 0 24 24"><circle cx="12" cy="12" r="10" fill="var(--gold)"/><path d="M2 12h20M12 2c3 3 3 17 0 20M12 2c-3 3-3 17 0 20" fill="none" stroke="var(--card-black)" stroke-width="1.5"/></svg>
        www.pwrkitchens.com
      </li>
    </ul>
    <div class="company-line">Pinewater Hospitality Group</div>
  </section>
</main>
</body>
</html>
```